VERUSO - PIZZA - RESTAURANT PIZZERIA

Flyer format:
- A5 front / back leaflet (Example attachment)
Customer logos:
- Attachment, VERUSO PIZZA logo
Address and contact to put on the flyers:
- Phone to add: (+352) 26 58 07 31 (Page 1)
- Address to be added: 8 rue des tilleuls, L-3592 Kayl, Luxembourg (Page 1)
- Website: www.veruso-example.lu (Page 1)
- Leave a space for the timetable (last page)
Flyer color:
- Preferably black background with colored customer logo
Typefaces:
- At your convenience
Descriptions:
- We would like to have a flyer to the one we have put as an example in the attachment
Important elements:
- Pizza oven on the cover page with customer logo, address and contact details
- The graphic elements must be usable and non-paying, we want a quality visual.
- Menu (attachment) The menu is in Word format, it must be laid out in a thoughtful way as on the example model.
- We need to find some pizza and/or ingredient visuals
Aspects :
- The design of the set must be elegant, sober and must contain all the information (Menu, visual of your choice, logo)

Target Market(s)

Private and professional public

Font styles to use
Serif
Sans Serif

Requirements
Must have
• Elegance, take into account the information of the comment
Nice to have
• Pizza oven, Dominant color black, Gold, red
Should not have
• poor quality visuals

```html
<!DOCTYPE html>
<html lang="fr">
<head>
<meta charset="utf-8">
<title>Veruso Pizza – Dépliant A5</title>
<link href="https://fonts.googleapis.com/css2?family=Roboto:wght@300;400;500;700&family=Roboto+Condensed:wght@400;700&display=swap" rel="stylesheet">
<style>
  :root{
    --stage:#e8e8e8;
    --page:#1c1c1c;
    --page-dark:#121212;
    --frame:#cfcfcf;
    --white:#f2f2f2;
    --gold:#e2b33a;
    --gold-soft:#c9a13a;
    --red:#d1103a;
    --crimson:#c4124a;
    --pink:#e0205f;
  }
  *{margin:0;padding:0;box-sizing:border-box}
  html,body{width:1200px;height:1007px;overflow:hidden;background:var(--stage)}
  body{font-family:"Roboto",Arial,sans-serif;color:var(--white)}
  .leaflet{position:absolute;left:0;top:79px;width:1200px;height:849px;display:flex}
  .page{position:relative;width:600px;height:849px;background:linear-gradient(160deg,#242424 0%,var(--page) 45%,var(--page-dark) 100%);overflow:hidden}
  .page + .page{border-left:1px solid #3a3a3a}
  .page-frame{position:absolute;inset:15px;border:1px solid var(--frame);border-radius:16px;opacity:.7}
  .abs{position:absolute}

  .heading{font-family:"Roboto Condensed","Roboto",sans-serif;font-weight:700;font-size:24px;line-height:28px;letter-spacing:.2px;color:var(--white);white-space:nowrap}
  .rule{position:absolute;height:2px;background:linear-gradient(90deg,transparent,var(--gold) 20%,var(--gold) 80%,transparent)}
  .flourish{position:absolute;width:96px;height:18px;border-radius:9px;background:radial-gradient(ellipse at center,var(--gold) 0%,var(--gold-soft) 45%,transparent 75%);opacity:.85}

  .price-badge{position:absolute;width:125px;height:64px;border-radius:50%;background:radial-gradient(ellipse at 50% 35%,var(--pink),var(--crimson) 70%,#9e0d39);display:flex;align-items:center;justify-content:center;font-weight:700;font-size:25px;color:#fff}
  .drink-list{font-size:15.5px;line-height:21px;font-weight:400;color:var(--white);white-space:nowrap}
  .drinks-visual{position:absolute;left:443px;top:81px;width:84px;height:162px;border-radius:10px;background:linear-gradient(90deg,#e88a1e 0%,#e88a1e 35%,#b3121f 36%,#7a0a13 100%)}
  .red-line{position:absolute;left:47px;top:332px;width:494px;height:2px;background:linear-gradient(90deg,var(--red),var(--red) 80%,transparent)}

  .col-title{font-family:"Roboto Condensed","Roboto",sans-serif;font-weight:700;font-size:16px;color:var(--red)}
  .menu-col{position:absolute;list-style:none;font-size:15px;color:var(--white)}
  .menu-col li{white-space:nowrap}
  .menu-col b{font-weight:700;margin-left:6px}
  .col-cheese li{height:19.5px;line-height:19.5px}
  .col-meat li{height:18.3px;line-height:18.3px}
  .col-veg li{height:23.6px;line-height:23.6px}

  .info-box{position:absolute;left:49px;top:694px;width:488px;height:135px;border:2px solid var(--gold-soft);display:flex;align-items:center}
  .info-box p{flex:1;text-align:center;font-family:"Roboto Condensed","Roboto",sans-serif;font-weight:700;font-size:12.5px;line-height:16px;color:var(--gold);text-transform:uppercase;padding:0 18px}
  .info-divider{width:2px;height:72px;background:var(--red)}

  .cutlery-sketch{position:absolute;left:16px;top:16px;width:100px;height:150px;border-radius:14px 0 0 0;background:radial-gradient(ellipse at 40% 40%,rgba(200,200,200,.12),transparent 70%)}
  .brand{position:absolute;left:0;width:600px;text-align:center;font-weight:500;color:var(--gold)}
  .brand-name{top:50px;font-size:92px;line-height:110px;letter-spacing:4px}
  .brand-sub{top:168px;font-size:26px;letter-spacing:22px;padding-left:150px}
  .cover-visual{position:absolute;left:30px;top:250px;width:540px;height:440px;border-radius:28px;background:radial-gradient(ellipse at 60% 70%,#e7c24f 0%,#c98a2a 26%,#5a4a3a 50%,#2a2a2a 72%,#1e1e1e 90%)}
  .contact{position:absolute;left:0;width:600px;text-align:center;font-weight:300;color:var(--gold);font-size:19px;white-space:nowrap}
  .contact-address{top:726px}
  .contact-line{top:766px}
  .contact-line .sep{margin:0 12px}
  .contact-rule{position:absolute;left:190px;top:757px;width:220px;height:1px;background:linear-gradient(90deg,transparent,var(--red),transparent)}
</style>
</head>
<body>
<main class="leaflet">

  <section class="page page-menu">
    <div class="page-frame"></div>

    <h2 class="heading abs" style="left:48px;top:30px">BOISSONS 33CL</h2>
    <div class="rule" style="left:47px;top:64px;width:175px"></div>
    <div class="flourish" role="img" aria-label="Ornement doré" style="left:80px;top:66px"></div>
    <div class="price-badge" style="left:301px;top:17px">2,50€</div>
    <p class="drink-list abs" style="left:48px;top:98px">Kolaro, kolaro zero, kolaro cherry, fizzo,limeo sunnypack,<br>eau,teavia,frutalia,frutalia pomme cassis</p>

    <h2 class="heading abs" style="left:48px;top:165px">BOISSONS BOUTEILLE</h2>
    <div class="rule" style="left:47px;top:199px;width:175px"></div>
    <div class="flourish" role="img" aria-label="Ornement doré" style="left:80px;top:201px"></div>
    <div class="price-badge" style="left:301px;top:163px">5,50 €</div>
    <div class="drinks-visual" role="img" aria-label="Photo d'une canette orange et d'une bouteille de soda rouge"></div>
    <p class="drink-list abs" style="left:48px;top:232px">Kolaro, fizzo, acqua vellino ,teavia</p>

    <h2 class="heading abs" style="left:48px;top:268px">ALCOOLS ET VIN</h2>
    <div class="rule" style="left:47px;top:300px;width:175px"></div>
    <div class="flourish" role="img" aria-label="Ornement doré" style="left:85px;top:302px"></div>

    <div class="red-line"></div>

    <h2 class="heading abs" style="left:48px;top:346px">SUPPLEMENTS</h2>
    <div class="rule" style="left:47px;top:378px;width:175px"></div>
    <div class="flourish" role="img" aria-label="Ornement doré" style="left:85px;top:380px"></div>

    <h3 class="col-title abs" style="left:47px;top:403px">FROMAGES</h3>
    <ul class="menu-col col-cheese" style="left:47px;top:423px">
      <li>Mozza <b>1,50€</b></li><li>Burrata <b>3,50€</b></li><li>Buffala <b>5€</b></li>
      <li>Câpre <b>1,50€</b></li><li>Chevre <b>2€</b></li><li>Ail <b>1€</b></li>
      <li>St nectaire <b>2,50€</b></li><li>Olive <b>1€</b></li><li>Gorgonzola <b>2€</b></li>
      <li>Anchois <b>1,50€</b></li><li>Parmesan <b>2,50€</b></li><li>Ricotta <b>2€</b></li>
      <li>Ananas <b>2€</b></li>
    </ul>

    <h3 class="col-title abs" style="left:207px;top:403px">VIANDES</h3>
    <ul class="menu-col col-meat" style="left:207px;top:423px">
      <li>Poulet <b>2,50€</b></li><li>Viande hachee <b>2,50€</b></li><li>Merguez <b>2,50€</b></li>
      <li>Jambon cuit <b>2€</b></li><li>Lardon <b>2€</b></li><li>Jambon de parme <b>3,50€</b></li>
      <li>Thon <b>2€</b></li><li>Saumon <b>3,50€</b></li><li>Chorizo <b>2,50€</b></li>
      <li>Fruit de mer <b>3,50€</b></li><li>Scampi <b>3,50€</b></li><li>Andouillette <b>2€</b></li>
      <li>Jambon cru <b>2€</b></li>
    </ul>

    <h3 class="col-title abs" style="left:404px;top:403px">LEGUMES</h3>
    <ul class="menu-col col-veg" style="left:404px;top:424px">
      <li>Poivron <b>1,50€</b></li><li>Champignon <b>2€</b></li><li>Oignon <b>1,50€</b></li>
      <li>Pomme de terre <b>2€</b></li><li>Aubergine <b>2€</b></li><li>Artichaud <b>1,50€</b></li>
      <li>Courgette <b>2€</b></li><li>Œuf <b>1€</b></li><li>Roquette <b>2€</b></li>
      <li>Tomate cerise <b>2€</b></li><li>Pistache <b>1€</b></li>
    </ul>

    <div class="info-box">
      <p>Lorem ipsum dolor sit amet, consectetur adipiscing elit, sed do eiusmod tempor incid idunt ut labore et dolore</p>
      <span class="info-divider"></span>
      <p>Lorem ipsum dolor sit amet, consectetur adipiscing elit, sed do eiusmod tempor incid idunt ut labore et dolore</p>
    </div>
  </section>

  <section class="page page-cover">
    <div class="page-frame"></div>
    <div class="cutlery-sketch" role="img" aria-label="Croquis de couverts à la craie"></div>

    <div class="brand brand-name">VERUSO</div>
    <div class="brand brand-sub">PIZZA</div>

    <div class="cover-visual" role="img" aria-label="Illustration d'un four à pizza en briques avec flammes, une pizza au salami sur une pelle et des tomates dessinées"></div>

    <p class="contact contact-address">8 rue des tilleuls, L-3592 Kayl, Luxembourg</p>
    <div class="contact-rule"></div>
    <p class="contact contact-line">(+352) 26 58 07 31<span class="sep">|</span>www.veruso-example.lu</p>
    <div class="rule" style="left:230px;top:802px;width:140px"></div>
    <div class="flourish" role="img" aria-label="Ornement doré" style="left:252px;top:804px"></div>
  </section>

</main>
</body>
</html>
```